Quill Forge Solutions
Bold and Unique
Project: Quill Forge Solutions
Quill Forge Solutions -
Creative Brief
Simple
Gary Holbrook
Owner / IT Consultant
Gary@TheQuillForge.com
www.TheQuillForge.com
Please use either black and white, or black and red if you can... but if you find something that works better, than that works too!! Please be as creative and bold as possible!

```html
<!DOCTYPE html>
<html lang="en">
<head>
<meta charset="utf-8">
<title>Quill Forge Solutions – Business Card</title>
<link href="https://fonts.googleapis.com/css2?family=Arimo:wght@400;700&display=swap" rel="stylesheet">
<style>
  :root {
    --paper: #ffffff;
    --card-edge: #8a8a8a;
    --ink: #000000;
    --red: #e3161d;
    --red-dark: #b50f14;
    --white: #ffffff;
    --light: #e6e6e6;
  }
  * { margin: 0; padding: 0; box-sizing: border-box; }
  html, body { width: 1200px; height: 850px; overflow: hidden; background: var(--paper); }
  body { position: relative; font-family: "Arimo", Arial, sans-serif; }

  .card {
    position: absolute;
    background: var(--paper);
    border: 2px solid var(--card-edge);
    overflow: hidden;
  }
  .card--front { left: 120px; top: 65px; width: 577px; height: 346px; }
  .card--back  { left: 540px; top: 436px; width: 571px; height: 349px; }

  .band {
    position: absolute; left: 0; right: 0;
    background: var(--ink);
  }
  .band::before, .band::after {
    content: ""; position: absolute; left: 0; right: 0;
    background: linear-gradient(to bottom, var(--red), var(--red-dark));
  }
  .band::before { top: 0; height: 6px; }
  .band::after  { bottom: 0; height: 13px; }
  .card--front .band { top: 66px; height: 209px; }
  .card--back  .band { top: 72px; height: 205px; }

  /* front */
  .brand {
    position: absolute; left: 0; right: 0; top: 101px;
    display: flex; flex-direction: column; align-items: center; gap: 20px;
  }
  .brand__mark {
    width: 68px; height: 68px; border-radius: 50%;
    background: var(--red);
  }
  .brand__name {
    color: var(--white); font-weight: 700; font-size: 25px;
    letter-spacing: 2px; text-transform: uppercase;
  }

  /* back */
  .person { position: absolute; left: 58px; top: 126px; }
  .person__name { color: var(--white); font-weight: 700; font-size: 24px; }
  .person__role { color: var(--red); font-size: 15px; margin-top: 2px; }

  .divider {
    position: absolute; left: 293px; top: 116px; width: 2px; height: 78px;
    background: var(--light);
  }

  .contacts { position: absolute; left: 322px; top: 117px; list-style: none; }
  .contacts li {
    display: flex; align-items: center; gap: 10px;
    color: var(--white); font-weight: 700; font-size: 15px; height: 25px;
  }
  .contacts svg { width: 14px; height: 14px; fill: var(--red); flex: none; }

  .tagline {
    position: absolute; left: 0; right: 0; top: 222px; text-align: center;
    color: var(--white); font-weight: 700; font-size: 18px;
  }
</style>
</head>
<body>
  <section class="card card--front">
    <div class="band"></div>
    <div class="brand">
      <span class="brand__mark"></span>
      <span class="brand__name">Quill Forge Solutions</span>
    </div>
  </section>

  <section class="card card--back">
    <div class="band"></div>
    <div class="person">
      <p class="person__name">Gary Holbrook</p>
      <p class="person__role">Owner/IT Consultant</p>
    </div>
    <div class="divider"></div>
    <ul class="contacts">
      <li>
        <svg viewBox="0 0 24 24" aria-hidden="true"><path d="M6.6 10.8a15.1 15.1 0 0 0 6.6 6.6l2.2-2.2c.3-.3.7-.4 1-.2 1.1.4 2.3.6 3.6.6.6 0 1 .4 1 1V20c0 .6-.4 1-1 1A17 17 0 0 1 3 4c0-.6.4-1 1-1h3.5c.6 0 1 .4 1 1 0 1.3.2 2.5.6 3.6.1.3 0 .7-.2 1z"/></svg>
        <span>5550142386</span>
      </li>
      <li>
        <svg viewBox="0 0 24 24" aria-hidden="true"><path d="M2 5h20v14H2z M4 7v.5l8 5 8-5V7l-8 5z" fill-rule="evenodd"/></svg>
        <span>Gary@TheQuillForge.com</span>
      </li>
      <li>
        <svg viewBox="0 0 24 24" aria-hidden="true"><path d="M12 2a10 10 0 1 0 0 20 10 10 0 0 0 0-20zm0 2c.9 1.2 1.6 2.6 2 4h-4c.4-1.4 1.1-2.8 2-4zM4.3 14a8 8 0 0 1 0-4h3.4a16 16 0 0 0 0 4zm1 2h3c.3 1.3.8 2.5 1.4 3.6A8 8 0 0 1 5.3 16zm3-8h-3a8 8 0 0 1 4.4-3.6C9 5.5 8.6 6.7 8.3 8zM12 20c-.9-1.2-1.6-2.6-2-4h4c-.4 1.4-1.1 2.8-2 4zm2.3-6H9.7a14 14 0 0 1 0-4h4.6a14 14 0 0 1 0 4zm.4 5.6c.6-1.1 1.1-2.3 1.4-3.6h3a8 8 0 0 1-4.4 3.6zm1.6-5.6a16 16 0 0 0 0-4h3.4a8 8 0 0 1 0 4z"/></svg>
        <span>www.TheQuillForge.com</span>
      </li>
    </ul>
    <p class="tagline">Strength &amp; Clarity in Craft</p>
  </section>
</body>
</html>
```